GLP letterhead

We need a letterhead design for our new company based in Los Angeles called "Gold Lantern Pictures". We develop film and television projects. We work with investors, financiers, film production companies, film distribution and sales companies as well as studios. We would like to incorporate our logo (see attached) but make the letterhead simple and elegant. We need to include: logo, company address, phone number and company website.
Updates

Hello designers, Thanks for your submissions. For our letterhead, we are looking for something more simple and elegant. No heavy bars or lines. Make it feel light and clean. Not a lot of ink on the page. Use the logo and contact info but think "clean", "streamlined" and mostly white paper. Looking forward to seeing more... thanks! Gold Lantern Pictures team

Target Market(s)

Studio executives, talent agents and agencies, financiers, investors.

Industry/Entity Type

It Company

Requirements
Must have
• Gold Lantern Pictures logo (see attached). Logo may be cropped and altered appropriately for elegant letterhead design.
• Please include:
• COMPANY ADDRESS:
• Ridgeway Studio Park
• 2850 Halverson Street
• Tower Annex, Suite 12
• Lakemont Heights, NV 89512
• COMPANY WEBSITE:
• www.goldlanternpicturesco.example
• COMPANY PHONE NUMBER:
• 555-555-0148

```html
<!DOCTYPE html>
<html lang="en">
<head>
<meta charset="utf-8">
<title>Gold Lantern Pictures – Stationery</title>
<link href="https://fonts.googleapis.com/css2?family=Ubuntu:wght@400;500;700&display=swap" rel="stylesheet">
<style>
  :root {
    --backdrop: #ebebeb;
    --paper: #ffffff;
    --ink: #1a1a1a;
    --black: #000000;
    --card-dark: #231f20;
    --brand-blue: #1fa3d6;
    --orb: #0e4256;
    --shadow: 3px 3px 4px rgba(0,0,0,0.45);
  }
  * { margin: 0; padding: 0; box-sizing: border-box; }
  html, body { width: 1200px; height: 1000px; overflow: hidden; }
  body {
    position: relative;
    background: var(--backdrop);
    font-family: "Ubuntu", sans-serif;
    color: var(--ink);
  }
  p { white-space: nowrap; }
  .sheet { position: absolute; box-shadow: var(--shadow); }

  /* Letterhead */
  .letterhead { left: 130px; top: 185px; width: 416px; height: 588px; background: var(--paper); }
  .letterhead .head { position: absolute; left: 179px; top: 19px; font-size: 8.5px; font-weight: 700; }
  .letterhead .address { position: absolute; left: 179px; top: 36px; font-size: 6.5px; line-height: 9.5px; }
  .letterhead .contact { position: absolute; left: 285px; top: 36px; font-size: 6.5px; line-height: 9.5px; }
  .letterhead .brand-block { left: 27px; top: 443px; width: 122px; height: 121px; }

  /* Brand block */
  .brand-block {
    position: absolute; background: var(--black);
    display: flex; flex-direction: column; align-items: center; justify-content: center;
  }
  .brand-block .orb { border-radius: 50%; background: var(--orb); }
  .brand-block .brand-name {
    color: var(--brand-blue); font-weight: 500; text-align: center;
    letter-spacing: 0.05em; text-transform: uppercase; line-height: 1.2; white-space: nowrap;
  }
  .letterhead .orb { width: 60px; height: 60px; margin-bottom: 10px; }
  .letterhead .brand-name { font-size: 8px; }

  /* Envelope front */
  .envelope-front { left: 474px; top: 331px; width: 436px; height: 217px; background: var(--paper); }
  .envelope-front .brand-block { left: 15px; top: 122px; width: 79px; height: 79px; }
  .envelope-front .orb { width: 40px; height: 40px; margin-bottom: 6px; }
  .envelope-front .brand-name { font-size: 5.5px; }

  /* Envelope back */
  .envelope-back { left: 474px; top: 605px; width: 436px; height: 217px; background: var(--black); color: var(--paper); }
  .envelope-back .flap { position: absolute; left: 0; top: 0; }
  .envelope-back .brand-block { left: 20px; top: 105px; width: 100px; height: 90px; background: transparent; }
  .envelope-back .orb { width: 52px; height: 52px; margin-bottom: 7px; }
  .envelope-back .brand-name { font-size: 6.5px; }
  .envelope-back .head { position: absolute; left: 129px; top: 131px; font-size: 7.5px; font-weight: 700; }
  .envelope-back .address { position: absolute; left: 129px; top: 141px; font-size: 6px; line-height: 7.5px; }
  .envelope-back .web { position: absolute; left: 129px; top: 178px; font-size: 6.5px; font-weight: 700; }

  /* Business card front */
  .card-front { left: 635px; top: 185px; width: 182px; height: 107px; background: var(--paper); }
  .card-front .person { position: absolute; left: 58px; top: 14px; font-size: 7.5px; font-weight: 700; }
  .card-front .role { position: absolute; left: 58px; top: 23px; font-size: 6px; }
  .card-front .email { position: absolute; left: 58px; top: 31px; font-size: 5.5px; }
  .card-front .head { position: absolute; left: 58px; top: 48px; font-size: 5px; font-weight: 700; }
  .card-front .address { position: absolute; left: 58px; top: 54px; font-size: 5px; line-height: 6.5px; }
  .card-front .web { position: absolute; left: 58px; top: 87px; font-size: 5px; font-weight: 700; }
  .card-front .brand-block { left: 15px; top: 62px; width: 33px; height: 33px; }
  .card-front .orb { width: 16px; height: 16px; margin-bottom: 3px; }
  .card-front .brand-name { font-size: 2.6px; }

  /* Business card back */
  .card-back { left: 855px; top: 185px; width: 182px; height: 107px; background: var(--card-dark); }
  .card-back .brand-block { left: 0; top: 0; width: 182px; height: 107px; background: transparent; }
  .card-back .orb { width: 56px; height: 56px; margin-bottom: 8px; }
  .card-back .brand-name { font-size: 8px; }
</style>
</head>
<body>

  <section class="sheet letterhead" aria-label="Letterhead">
    <p class="head">Ridgeway Studio Park</p>
    <p class="address">2850 Halverson Street<br>Tower Annex, Suite 12<br>Lakemont Heights, NV 89512</p>
    <p class="contact">P: 555-555-0148<br>www.goldlanternpicturesco.example</p>
    <div class="brand-block">
      <span class="orb"></span>
      <span class="brand-name">Gold Lantern<br>Pictures</span>
    </div>
  </section>

  <section class="sheet card-front" aria-label="Business card front">
    <p class="person">Nora Whitfield</p>
    <p class="role">Director</p>
    <p class="email">nora@goldlanternpicturesco.example</p>
    <p class="head">Ridgeway Studio Park</p>
    <p class="address">2850 Halverson Street<br>Tower Annex, Suite 12<br>Lakemont Heights, NV 89512<br>Phone: 555-555-0148</p>
    <p class="web">www.goldlanternpicturesco.example</p>
    <div class="brand-block">
      <span class="orb"></span>
      <span class="brand-name">Gold Lantern<br>Pictures</span>
    </div>
  </section>

  <section class="sheet card-back" aria-label="Business card back">
    <div class="brand-block">
      <span class="orb"></span>
      <span class="brand-name">Gold Lantern Pictures</span>
    </div>
  </section>

  <section class="sheet envelope-front" aria-label="Envelope front">
    <div class="brand-block">
      <span class="orb"></span>
      <span class="brand-name">Gold Lantern<br>Pictures</span>
    </div>
  </section>

  <section class="sheet envelope-back" aria-label="Envelope back">
    <svg class="flap" width="436" height="82" viewBox="0 0 436 82">
      <polygon points="0,0 436,0 414,82 22,82" fill="#ffffff"/>
    </svg>
    <div class="brand-block">
      <span class="orb"></span>
      <span class="brand-name">Gold Lantern<br>Pictures</span>
    </div>
    <p class="head">Ridgeway Studio Park</p>
    <p class="address">2850 Halverson Street<br>Tower Annex, Suite 12<br>Lakemont Heights, NV 89512<br>Phone: 555-555-0148</p>
    <p class="web">www.goldlanternpicturesco.example</p>
  </section>

</body>
</html>
```